Halloway Crest Backers Guild business cards

Create a single-sided business card for the Halloway Crest Backers Guild based on the attached logo.
The additional data fields include Name, Title, Email, Phone, and website.
Please use the following as sample data:
Name: Dean Varrow
Title: Co-Founder / Investor
Email: deanvarrow@mailtern.net
Phone: 555-314-2706
Website: www.hcbackersguild.com

Target Market(s)

Start ups, entrepreneurs, venture capitalists

Industry/Entity Type

Investment

Contact Information for Business Card

Professional business card. Technology company.

Font styles to use
Serif
Sans Serif

Requirements
Must have
• Include the HCBG logo (attached)
• Name
• Title
• Email
• Phone
• Website
Should not have
• Cute, cartoony

```html
<!DOCTYPE html>
<html lang="en">
<head>
<meta charset="utf-8">
<title>Halloway Crest Backers Guild – Business Card</title>
<link href="https://fonts.googleapis.com/css2?family=Open+Sans:wght@400;600;700&display=swap" rel="stylesheet">
<style>
  :root {
    --green: #22a565;
    --green-dark: #1b8f55;
    --grey: #4a4a4a;
    --white: #ffffff;
    --paper: #fbfbfb;
    --backdrop: #e9e9e9;
  }
  * { margin: 0; padding: 0; box-sizing: border-box; }
  html, body {
    width: 1200px; height: 1022px; overflow: hidden;
    background: var(--backdrop);
    font-family: "Open Sans", Arial, sans-serif;
  }
  .card {
    position: absolute; left: 100px; top: 225px;
    width: 1000px; height: 572px;
    background: var(--paper);
    border-radius: 26px;
    overflow: hidden;
    box-shadow: 0 10px 30px rgba(0,0,0,0.15);
  }
  .card-sweep { position: absolute; inset: 0; }
  .contact {
    position: absolute; left: 64px; top: 300px;
    color: var(--white);
  }
  .contact-name { font-size: 40px; font-weight: 700; letter-spacing: 0.5px; }
  .contact-title { font-size: 24px; font-weight: 400; margin-bottom: 14px; color: var(--grey); }
  .contact-line {
    display: flex; align-items: center; gap: 14px;
    font-size: 22px; font-weight: 400; line-height: 38px;
  }
  .contact-line svg { width: 18px; height: 18px; flex: none; }
  .brand {
    position: absolute; left: 600px; top: 236px;
    display: flex; align-items: center; gap: 18px;
  }
  .brand-square { width: 22px; height: 22px; background: var(--green); }
  .brand-name {
    font-size: 34px; font-weight: 600; line-height: 1.15;
    color: var(--green); width: 340px;
  }
</style>
</head>
<body>
  <article class="card">
    <svg class="card-sweep" viewBox="0 0 1000 572" aria-hidden="true">
      <path d="M0,0 H300 C440,150 460,420 380,572 H0 Z" fill="var(--green)"/>
      <path d="M318,0 C458,150 478,420 398,572" fill="none" stroke="var(--grey)" stroke-width="9"/>
      <path d="M336,0 C476,150 496,420 416,572" fill="none" stroke="var(--green)" stroke-width="3"/>
    </svg>

    <section class="contact">
      <div class="contact-name">Dean Varrow</div>
      <div class="contact-title">Co-Founder / Investor</div>
      <div class="contact-line">
        <svg viewBox="0 0 24 24"><path d="M6 2l4 4-2 3c1 3 4 6 7 7l3-2 4 4-3 4C10 22 2 14 2 5z" fill="var(--white)"/></svg>
        <span>555-314-2706</span>
      </div>
      <div class="contact-line">
        <svg viewBox="0 0 24 24"><rect x="2" y="5" width="20" height="14" fill="none" stroke="var(--white)" stroke-width="2"/><path d="M2 5l10 8 10-8" fill="none" stroke="var(--white)" stroke-width="2"/></svg>
        <span>deanvarrow@mailtern.net</span>
      </div>
      <div class="contact-line">
        <svg viewBox="0 0 24 24"><circle cx="12" cy="12" r="10" fill="none" stroke="var(--white)" stroke-width="2"/><path d="M2 12h20M12 2c4 4 4 16 0 20M12 2c-4 4-4 16 0 20" fill="none" stroke="var(--white)" stroke-width="1.6"/></svg>
        <span>www.hcbackersguild.com</span>
      </div>
    </section>

    <div class="brand">
      <span class="brand-square"></span>
      <span class="brand-name">Halloway Crest Backers Guild</span>
    </div>
  </article>
</body>
</html>
```